User DashBoard and White Label Admin

The Project Contains two aspects I) User screens and II) White Label Admin Screens

I) User Screens:
---------------------------------------------------------------------------------------------------------
Criteria :

Should be a unique layout with Crisper Images, fonts , Look & Feel should be eye catching, pleasing and most user friendly with great user experience."having the ability to display the following sections.

Target Audience: 18 - 40 years , most of the users would be with in the age group of 18-30.

1) Registration Page
2) Log in Page
3) Dash Board
4) Profile Management and settings
5) Reports
6) Shout Box -- Similar to that of Tandem Up feed or Lumo Page Feed.
7) Viral Marketing - Ability to invite friends to join the site

Detailed Steps involved for each module

1) Registration Page :

-The ability to register by using his Email/Phone No or lumoPage
- A validation screen for entered Email and Phone no
- Screen to answer a set of questions which form the basic input criteria and will be part of the profile management once the User Logs in
- Link to terms and conditions and other relevant items which fall as part of registration

2) Log In page :

- The ability to enter the Email/PhoneNO and password with Login specific details associated

3 )User Dash Board :
Mandatory Sections in the Dash Board :

a) Profile of the User
This should display the Photo , Email Id, Phone No and profile completion status
b) Ability to display Loyalty Points earned ( This should be the BOLD and Highlighted)
c) Ability to Display the Redeemed Cash based on the loyalty points earned ( This should be the BOLD and Highlighted)
d) Ability to Show the Show the Friends list which is fetched from Lumopage
e) Ability to show friends who have been invited and who have joined the site
f) Ability to show the top users of the product could be friends who have joined through referral/ any other medium or Lumopage
g) Link to Shout Box
h) Should be able to navigate to Profile Page if user wishes to edit the profile
i) Ability to answer the proforma which includes Demographics, Geographics, Interests etc
j)Ability to Display Brixo Ads
k) Ability to Promote offers of the Product
l) The user should be able to see "people he might know "

4) Profile Management and settings :
a) Ability to Edit his/her details
b) Ability to Go through the Set of questions which are part of proforma. The more the questions are answered the more the profile status bar will be updated.
c) Ability to display settings - similar to that of Lumo Page Settings

5) Reports:
a) Usage Details
b) Invited Friends Details
c) Etc
6) Shout Box :
a) Ability to Say what is going on in the users mind
b) Ability to see what the other users have posted

7) Viral marketing
a) Ability to invite friends by invoking social networking platforms/ emails etc.

II) Admin Screens
Criteria :

Should be a unique layout with Crisper Images and fonts having the ability to display the following sections.

Enterprise look and Feel

Target Audience: Top level Managements of various companies such as CEO's/CFO's Delivery and business heads etc ....

1) Admin Dash Board
2) Reports
3) Advertisements
4) Settings

1) Admins Dash Board

a) Ability to Create and Campaign
When The Admin Opts to create a Campaign , Admin should be taken through a set of questions with most possible details being the name of the campaign, target audience age limit, geographic location details where the campaign will be hosted , and the at any given point the Admin can traverse between these steps .
The Snapshot of the questions answered should always be displayed from Previous steps
b) Ability to Edit Campaign
When The Admin Opts to Edit a Campaign , Admin should be taken through a set of questions with most possible details being the name of the campaign, target audience age limit, geographic location details where the campaign will be hosted , and the at any given point the Admin can traverse between these steps .
C) Ability to Delete a Campaign
d) Ability to View all the Running Campaigns

e) Ability to view the account snap shot

f) Ability to Navigate to detailed reports
g) Ability to Navigate to settings
h) Ability to Create users

2) Reports:
a) Ability to see the served Campaign /Ads and their details
b) Good Graphical representation of the reports..
c) User can select a specific date , week, month or a date rage

3) Advertisements :

When The Admin Opts to create an Ad, Admin should be taken through a set of questions with most possible details being the name of the Ad , target audience age limit, geographic location details where the campaign will be hosted , and the at any given point the Admin can traverse between these steps .

When The Admin Opts to Edit an Ad, Admin should be taken through a set of questions with most possible details being the name of the Ad , target audience age limit, geographic location details where the campaign will be hosted , and the at any given point the Admin can traverse between these steps .
C) Ability to Delete an Ad

4) Settings :

a) Display of Various setting related to mail alerts and other admin related settings

Reason: There are only few designs provided ..

Target Market(s)

User Screens :
Target Audience: 18 - 40 years , most of the users would be with in the age group of 18-30 both Male and Female

II) Admin Screens

Requirements
Must have
• I) User Screens:
• ---------------------------------------------------------------------------------------------------------
• Criteria :
• Should be a unique layout with Crisper Images, fonts , Look & Feel should be eye catching, pleasing and most user friendly with great user experience."having the ability to display the following sections.
• II) Admin Screens
• Criteria :
• Should be a unique layout with Crisper Images and fonts having the ability to display the following sections.
• Enterprise look and Feel
• Should be inclined towards HTML5 Design Standards
Nice to have
• More Fancy usage of HTML5 Widgets
Should not have
• Dull, And regular static stuff which we observe in the normal sites should not be present.

```html
<!DOCTYPE html>
<html lang="en">
<head>
<meta charset="utf-8">
<title>Zentro – User Dashboard</title>
<link href="https://fonts.googleapis.com/css2?family=Raleway:wght@400;500;600;700&family=Arimo:wght@400;700&display=swap" rel="stylesheet">
<style>
:root{
  --bg:#ebebeb;
  --card:#ffffff;
  --line:#e3e3e3;
  --green:#4f9f35;
  --green-dark:#3f8a28;
  --yellow-panel:#f7f2a6;
  --gold:#f7bf08;
  --text:#333333;
  --muted:#8a8a8a;
  --faint:#b4b4b4;
  --footer:#333333;
  --ad-bg:#fdf3e6;
  --ad-link:#1a0dab;
  --ad-url:#1e7b1e;
}
*{box-sizing:border-box;margin:0;padding:0}
html,body{width:1200px;height:911px;overflow:hidden;background:var(--bg)}
body{font-family:"Raleway",sans-serif;color:var(--text)}
.stage{position:relative;width:1300px;height:987px;transform:scale(.9231);transform-origin:0 0;background:var(--bg)}
.card{position:absolute;background:var(--card)}
.abs{position:absolute}

/* header */
.topbar{position:absolute;left:0;top:0;width:1300px;height:61px;background:var(--card)}
.brand{position:absolute;left:0;top:0;width:217px;height:61px;border-right:1px solid var(--line);display:flex;align-items:center;justify-content:center;gap:8px;font-weight:700;font-size:22px;color:var(--green)}
.brand .dot{width:16px;height:16px;background:var(--gold)}
.search{position:absolute;left:422px;top:16px;width:272px;height:26px;border-radius:13px;background:#eeeeee;font-size:11px;color:#666;padding:6px 12px}
.search svg{position:absolute;right:9px;top:5px}
.invite{position:absolute;left:888px;top:16px;width:106px;height:26px;background:var(--green);border-radius:3px;color:#fff;font-size:11px;font-weight:500;display:flex;align-items:center;justify-content:center;gap:5px}
.topsep{position:absolute;left:1027px;top:0;height:61px;border-left:1px solid var(--line)}
.toplink{position:absolute;top:22px;font-size:11px;font-weight:500;display:flex;align-items:center;gap:6px}

/* account panel */
.account{left:0;top:74px;width:216px;height:435px;background:var(--yellow-panel)}
.account h2{font-weight:400;font-size:18px;padding:28px 0 0 34px;height:74px;border-bottom:1px solid #e5dd86}
.menu{list-style:none;padding:24px 0 0 34px}
.menu li{height:38px;font-size:13px;display:flex;align-items:center;gap:10px}
.menu svg{width:13px;height:13px}

/* friends */
.friends{left:0;top:524px;width:216px;height:391px}
.card-head{height:44px;border-bottom:1px solid var(--line);display:flex;align-items:center;justify-content:space-between;padding:0 18px 0 23px;font-size:15px}
.card-head.upper{font-size:14px;text-transform:uppercase;font-weight:500}
.online{display:flex;justify-content:space-between;padding:12px 18px 6px 23px;font-size:14px}
.person{display:flex;gap:10px;align-items:center;padding:0 0 0 23px;height:40px}
.avatar{width:30px;height:30px;background:linear-gradient(135deg,#c98a72,#6b4437);flex:none}
.person .nm{font-size:15px}
.person .ls{font-size:8px;color:var(--faint)}
.friend-list{border-top:1px solid var(--line);margin-top:9px;padding:14px 0 0 24px;font-size:12px;line-height:20px;position:relative}
.scroll{position:absolute;right:26px;top:18px;width:2px;height:92px;background:#ddd}
.scroll i{display:block;width:2px;height:42px;margin-top:18px;background:#333}

/* profile */
.profile{left:231px;top:74px;width:190px;height:473px}
.photo{width:190px;height:190px;background:linear-gradient(160deg,#c1523d 0%,#8d4a3c 45%,#2b2624 80%)}
.edit-badge{position:absolute;left:142px;top:12px;width:34px;height:34px;background:var(--green);color:#fff;font-size:6px;text-align:center;padding-top:4px}
.profile h3{font-size:15px;font-weight:600;margin:10px 0 0 13px}
.profile .loc{font-size:12px;color:#666;margin:4px 0 0 13px}
.contact{font-size:12px;color:#555;margin:16px 0 0 13px;line-height:20px}
.contact div{display:flex;gap:7px;align-items:center}
.completion{font-size:12px;margin:30px 0 0 13px}
.ring{position:absolute;left:44px;top:350px}

/* dialer */
.caller{left:231px;top:562px;width:190px;height:353px}
.numfield{position:absolute;left:17px;top:54px;width:156px;height:28px;border:1px solid #ddd;font-size:13px;color:#888;padding:6px 10px}
.keys{position:absolute;left:17px;top:94px;display:grid;grid-template-columns:repeat(3,46px);gap:9px}
.keys span{height:35px;background:var(--green);color:#fff;font-size:19px;display:flex;align-items:center;justify-content:center;border-bottom:2px solid var(--green-dark)}
.backspace{position:absolute;left:17px;top:276px;width:156px;height:28px;background:#d8d8d8;color:#fff;font-size:11px;display:flex;align-items:center;justify-content:center}
.callnow{position:absolute;left:17px;top:310px;width:156px;height:28px;background:var(--gold);color:#fff;font-size:11px;font-weight:500;display:flex;align-items:center;justify-content:center;gap:6px}

/* shout box */
.shout{left:435px;top:74px;width:594px;height:190px}
.shout-area{position:absolute;left:14px;top:14px;width:406px;height:106px;border:1px solid #e2e2e2;font-size:14px;color:#888;font-style:italic;padding:12px 16px}
.shout-area b{color:#666;font-weight:600}
.tools{position:absolute;left:14px;top:119px;display:flex}
.tools span{width:29px;height:30px;border:1px solid #e2e2e2;border-top:none;display:flex;align-items:center;justify-content:center}
.submit{position:absolute;left:335px;top:148px;width:86px;height:25px;background:#e8e8e8;border-radius:3px;font-size:13px;color:#555;display:flex;align-items:center;justify-content:center}
.recent{position:absolute;left:434px;top:0;width:160px;height:190px;border-left:1px solid var(--line)}
.recent h4{font-weight:400;font-size:13px;padding:11px 14px;border-bottom:1px solid var(--line)}
.recent p{font-size:9px;color:#777;line-height:11px;margin:18px 20px 0 14px}

/* feed */
.feed{left:435px;top:277px;width:594px;height:230px}
.tabs{position:absolute;left:29px;top:14px;display:flex}
.tabs span{height:33px;border:1px solid #ddd;font-size:11.5px;display:flex;align-items:center;justify-content:center;padding:0 4px;margin-right:-1px;white-space:nowrap}
.tabs .on{background:var(--green);color:#fff;border-color:var(--green)}
.feed .rule{position:absolute;left:0;top:47px;width:594px;border-top:1px solid var(--line)}
.feed .pic{position:absolute;left:27px;top:65px;width:104px;height:103px;background:linear-gradient(135deg,#b78d6f,#7a513d)}
.byline{position:absolute;left:151px;top:64px;font-size:11px}
.byline b{font-weight:600}
.byline .meta{color:#888;font-size:10px;margin-left:26px}
.feed .body{position:absolute;left:151px;top:93px;width:420px;font-size:11.5px;color:#888;line-height:17px}
.feed .foot{position:absolute;left:0;top:186px;width:594px;height:44px;border-top:1px solid var(--line);font-size:12px;display:flex;align-items:center}

/* promote */
.promote{left:435px;top:521px;width:594px;height:229px}
.promote h3{position:absolute;left:26px;top:15px;font-size:15px;font-weight:500}
.products{position:absolute;left:26px;top:55px;display:flex;gap:16px}
.product{width:124px;text-align:center;font-size:11px}
.product .thumb{height:100px;border:1px solid #ddd}
.product .cap{margin-top:5px}
.product .btn{width:101px;height:20px;margin:7px auto 0;background:var(--green);color:#fff;font-size:12px;display:flex;align-items:center;justify-content:center;border-radius:2px}

/* ad */
.ad{left:435px;top:765px;width:594px;height:150px;background:var(--ad-bg);font-family:"Arimo",sans-serif}
.ad .label{position:absolute;left:24px;top:5px;font-size:12px;color:#555}
.ad .title{position:absolute;left:24px;top:26px;font-size:15px;color:var(--ad-link);text-decoration:underline}
.ad .url{position:absolute;left:24px;top:45px;font-size:13px;color:var(--ad-url)}
.ad .url span{color:#333;font-size:12px;margin-left:12px}
.ad .desc{position:absolute;left:24px;top:62px;font-size:13px;color:#333}
.ad .links{position:absolute;left:49px;top:83px;display:grid;grid-template-columns:246px 160px;font-size:12px;color:var(--ad-link);line-height:19px}

/* right column */
.points{left:1044px;top:74px;width:256px;height:190px}
.points h4{font-weight:500;font-size:14px;padding:12px 23px;border-bottom:1px solid var(--line)}
.stat{position:absolute;left:24px;display:flex;gap:10px}
.stat b{font-size:24px;font-weight:700;display:block}
.stat small{font-size:10px;color:var(--muted)}
.pymk{left:1044px;top:277px;width:256px;height:230px}
.grid2{display:grid;grid-template-columns:118px 118px;padding:14px 0 0 22px;row-gap:11px}
.mini{display:flex;gap:6px}
.mini .avatar{width:30px;height:33px}
.mini .nm{font-size:11px}
.mini .ls{font-size:8px;color:var(--faint)}
.top-users{left:1044px;top:521px;width:256px;height:394px}
.tu{height:69px;border-bottom:1px solid var(--line);display:flex;align-items:center;gap:12px;padding-left:24px}
.tu .avatar{width:31px;height:31px}
.tu .nm{font-size:14px}
.tu .ls{font-size:8px;color:var(--faint)}
.more{position:absolute;left:89px;top:353px;font-size:12px;font-weight:600;display:flex;gap:8px}

.footer{position:absolute;left:0;top:929px;width:1300px;height:58px;background:var(--footer);color:#fff;font-size:11px;text-align:center;line-height:58px}
</style>
</head>
<body>
<div class="stage">

<header class="topbar">
  <div class="brand"><span class="dot"></span>Zentro</div>
  <div class="search">Search
    <svg width="15" height="15" viewBox="0 0 15 15"><circle cx="6" cy="6" r="4.5" fill="none" stroke="#333" stroke-width="2"/><line x1="9.5" y1="9.5" x2="13.5" y2="13.5" stroke="#333" stroke-width="2"/></svg>
  </div>
  <div class="invite"><svg width="11" height="11"><path d="M4 0h3v4h4v3H7v4H4V7H0V4h4z" fill="#fff"/></svg>INVITE USER</div>
  <div class="topsep"></div>
  <div class="toplink" style="left:1058px"><svg width="15" height="15" viewBox="0 0 15 15"><circle cx="7.5" cy="7.5" r="5" fill="none" stroke="#5aa73c" stroke-width="3" stroke-dasharray="2 1.6"/><circle cx="7.5" cy="7.5" r="2" fill="#5aa73c"/></svg>SETTINGS</div>
  <div class="toplink" style="left:1170px"><svg width="15" height="15"><path d="M2 2l11 11M13 2L2 13" stroke="#5aa73c" stroke-width="3.5"/></svg>LOGOUT</div>
</header>

<nav class="card account">
  <h2>My Account Panel</h2>
  <ul class="menu">
    <li><svg viewBox="0 0 13 13"><circle cx="6.5" cy="4" r="3" fill="#333"/><path d="M1 13c0-4 11-4 11 0z" fill="#333"/></svg>Account &amp; Profile</li>
    <li><svg viewBox="0 0 13 13"><rect x="1" y="2" width="11" height="10" fill="#333"/></svg>Demographics</li>
    <li><svg viewBox="0 0 13 13"><path d="M12 1L1 6l5 1 1 5z" fill="none" stroke="#333" stroke-width="1.5"/></svg>Geographics</li>
    <li><svg viewBox="0 0 13 13"><path d="M4 1v11M9 1v11M1 4h11M1 9h11" stroke="#333" stroke-width="2"/></svg>Friendslist</li>
    <li><svg viewBox="0 0 13 13"><path d="M2 1v12M2 2h9l-2 3 2 3H2" fill="none" stroke="#333" stroke-width="1.6"/></svg>Interests</li>
    <li><svg viewBox="0 0 13 13"><circle cx="6.5" cy="6.5" r="5" fill="none" stroke="#333" stroke-width="1.6"/><path d="M6.5 6.5V1.5A5 5 0 0 1 11.5 6.5z" fill="#333"/></svg>Psychographics</li>
    <li><svg viewBox="0 0 13 13"><circle cx="2.5" cy="2.5" r="2" fill="#333"/><circle cx="10.5" cy="2.5" r="2" fill="#333"/><circle cx="2.5" cy="10.5" r="2" fill="#333"/><circle cx="10.5" cy="10.5" r="2" fill="#333"/><path d="M2.5 2.5l8 8M10.5 2.5v8" stroke="#333"/></svg>Networks</li>
    <li><svg viewBox="0 0 13 13"><path d="M2 2l9 9M11 2l-9 9" stroke="#333" stroke-width="2.6"/></svg>Logout</li>
  </ul>
</nav>

<section class="card friends">
  <div class="card-head">My Friends <svg width="17" height="17"><circle cx="7" cy="7" r="5.5" fill="none" stroke="#ccc" stroke-width="2"/><line x1="11" y1="11" x2="16" y2="16" stroke="#ccc" stroke-width="2"/></svg></div>
  <div class="online">Online Now <span style="color:#ccc">&lsaquo; <span style="color:#333;margin-left:26px">&rsaquo;</span></span></div>
  <div class="person"><div class="avatar" role="img" aria-label="Friend profile photo"></div><div><div class="nm">Nikka Sapphire</div><div class="ls">Last on: 5mins ago</div></div></div>
  <div class="person"><div class="avatar" role="img" aria-label="Friend profile photo"></div><div><div class="nm">Velika Spire</div><div class="ls">Last on: 5mins ago</div></div></div>
  <div class="person"><div class="avatar" role="img" aria-label="Friend profile photo"></div><div><div class="nm">Monika Spiral</div><div class="ls">Last on: 5mins ago</div></div></div>
  <div class="person"><div class="avatar" role="img" aria-label="Friend profile photo"></div><div><div class="nm">Velika Spire</div><div class="ls">Last on: 5mins ago</div></div></div>
  <div class="friend-list">Velika Spire<br>Alina Merrowvale<br>John Doe<br>Helen Smith<br>Jack Nile<div class="scroll"><i></i></div></div>
</section>

<section class="card profile">
  <div class="photo" role="img" aria-label="Profile photo of the user holding a camera"></div>
  <div class="edit-badge"><svg width="16" height="16"><rect x="1" y="3" width="12" height="12" fill="none" stroke="#fff" stroke-width="1.6"/><path d="M6 10l1-3 7-7 2 2-7 7z" fill="#fff"/></svg><br>EDIT</div>
  <h3>LARA SMITH</h3>
  <div class="loc">Currently in Atlanta</div>
  <div class="contact">
    <div><svg width="12" height="9"><rect width="12" height="9" fill="#5aa73c"/><path d="M0 0l6 5 6-5" stroke="#fff" fill="none"/></svg>lara.smith@mailbox.test</div>
    <div><svg width="12" height="12"><path d="M2 1l3 0 1 3-2 1c1 2 2 3 4 4l1-2 3 1v3C6 11 1 6 2 1z" fill="#5aa73c"/></svg>(001) 5550-1234-56</div>
  </div>
  <div class="completion">Profile Completion</div>
  <svg class="ring" width="104" height="104" viewBox="0 0 104 104">
    <circle cx="52" cy="52" r="47" fill="none" stroke="#fff" stroke-width="8"/>
    <circle cx="52" cy="52" r="47" fill="none" stroke="#4f9f35" stroke-width="8" stroke-dasharray="206.7 295.3" transform="rotate(-90 52 52)"/>
    <text x="52" y="59" text-anchor="middle" font-family="Raleway,sans-serif" font-size="20" fill="#333">70%</text>
  </svg>
</section>

<section class="card caller">
  <div class="card-head upper" style="font-weight:400">CALL FROM HERE</div>
  <div class="numfield">0015550198274</div>
  <div class="keys"><span>1</span><span>2</span><span>3</span><span>4</span><span>5</span><span>6</span><span>7</span><span>8</span><span>9</span><span>*</span><span>0</span><span>#</span></div>
  <div class="backspace">&larr;&nbsp; BACKSPACE</div>
  <div class="callnow"><svg width="11" height="11"><path d="M2 1l3 0 1 3-2 1c1 2 2 3 4 4l1-2 3 1v3C6 11 1 6 2 1z" fill="#fff"/></svg>CALL NOW</div>
</section>

<section class="card shout">
  <div class="shout-area"><b>Shout Box</b> - Say something</div>
  <div class="tools">
    <span><svg width="13" height="13"><path d="M1 12l1-4 7-7 3 3-7 7z" fill="#888"/></svg></span>
    <span><svg width="14" height="12"><rect x="1" y="1" width="12" height="10" fill="none" stroke="#888"/><path d="M2 10l4-4 3 3 2-2 2 3z" fill="#888"/></svg></span>
    <span><svg width="15" height="10"><rect width="10" height="10" fill="#888"/><path d="M10 5l5-4v8z" fill="#888"/></svg></span>
    <span><svg width="12" height="12"><circle cx="10" cy="2" r="2" fill="#888"/><circle cx="2" cy="6" r="2" fill="#888"/><circle cx="10" cy="10" r="2" fill="#888"/><path d="M10 2L2 6l8 4" stroke="#888" fill="none"/></svg></span>
  </div>
  <div class="submit">Submit</div>
  <aside class="recent">
    <h4>Recent Says</h4>
    <p>Lorem ipsum dolor sit amet, consectetur adipisi cing elit...</p>
    <p style="margin-top:14px">Duis aute irure dolor in reprehenderit in voluptate velit esse cillum dolore eu fugiat nulla...</p>
  </aside>
</section>

<section class="card feed">
  <div class="tabs"><span style="width:129px">LUMOPAGE FEEDS</span><span style="width:128px">SHOUT BOX</span><span class="on" style="width:129px">NOTIFICATIONS</span></div>
  <div class="rule"></div>
  <div class="pic" role="img" aria-label="Photo of the post author"></div>
  <div class="byline"><b>By Lana Smith</b><span class="meta">Paris, France &nbsp;|&nbsp; Dec 06 2013</span></div>
  <p class="body">Sed ut perspiciatis unde omnis iste natus error sit voluptatem accusantium doloremque laudantium, totam rem aperiam, eaque ipsa quae ab illo inventore veritatis et quasi architecto beatae vitae dicta sunt explicabo. Nemo enim ipsam voluptatem...</p>
  <div class="foot">
    <span style="margin-left:28px;color:#bbb;font-size:11px">&#9633; Public</span>
    <span style="margin-left:58px;font-weight:500"><span style="color:#aaa">&#9733;</span> Like this</span>
    <span style="margin-left:56px"><b>1,051</b> people liked this</span>
    <span style="margin-left:59px;font-weight:600">Full Article</span>
  </div>
</section>

<section class="card promote">
  <h3>Promote Your products</h3>
  <span class="abs" style="left:498px;top:12px;color:#ccc;font-size:20px">&lsaquo;</span>
  <span class="abs" style="left:560px;top:12px;font-size:20px">&rsaquo;</span>
  <div class="products">
    <div class="product"><div class="thumb" role="img" aria-label="Product photo: glass aquarium bowls" style="background:linear-gradient(#dfeee5,#8fbf9a)"></div><div class="cap">Lorem Ipsum Amet</div><div class="btn">Promote!</div></div>
    <div class="product"><div class="thumb" role="img" aria-label="Product photo: speakers on a desk" style="background:linear-gradient(#bdb3a8,#4a3a2e)"></div><div class="cap">Lorem Ipsum Amet</div><div class="btn">Promote!</div></div>
    <div class="product"><div class="thumb" role="img" aria-label="Product photo: water tap filling a glass" style="background:linear-gradient(#f2f2f2,#a9a9a9)"></div><div class="cap">Lorem Ipsum Amet</div><div class="btn">Promote!</div></div>
    <div class="product"><div class="thumb" role="img" aria-label="Product photo: round home thermostat" style="background:linear-gradient(#7b5a44,#2a2220)"></div><div class="cap">Lorem Ipsum Amet</div><div class="btn">Promote!</div></div>
  </div>
</section>

<section class="card ad">
  <div class="label">Ad related to <b>brixo ads</b> &#9432;</div>
  <div class="title"><b>Brixo Advertising</b> - <b>Brixo Ads</b> Can Grow Your Business</div>
  <div class="url">www.<b>brixo</b>.example/<b>AdSuite</b> &#9662;<span>900 55 12 34</span></div>
  <div class="desc">Only Pay When Your <b>Ad</b> is Clicked</div>
  <div class="links"><span>How It Works</span><span>Local Advertising</span><span>Start Now With AdSuite</span><span>Success Stories</span></div>
</section>

<section class="card points">
  <h4>MY POINTS &amp; CASH</h4>
  <div class="stat" style="top:56px"><svg width="24" height="18" style="margin-top:8px"><path d="M1 5l6 4 5-7 5 7 6-4-2 11H3z" fill="#f7bf08"/></svg><div><b>225,556</b><small>Loyalty Points Earned</small></div></div>
  <div class="stat" style="top:122px"><svg width="24" height="26" style="margin-top:4px"><circle cx="12" cy="16" r="9" fill="#f7bf08"/><path d="M8 2h8l-2 6h-4z" fill="#f7bf08"/><text x="12" y="20" text-anchor="middle" font-size="10" fill="#fff" font-family="Arial">$</text></svg><div><b>$30,556</b><small>Redeemed Cash</small></div></div>
</section>

<section class="card pymk">
  <div class="card-head upper" style="font-weight:400;height:41px">PEOPLE YOU MIGHT KNOW <svg width="17" height="17"><circle cx="7" cy="7" r="5.5" fill="none" stroke="#ccc" stroke-width="2"/><line x1="11" y1="11" x2="16" y2="16" stroke="#ccc" stroke-width="2"/></svg></div>
  <div class="grid2">
    <div class="mini"><div class="avatar" role="img" aria-label="Suggested person photo"></div><div><div class="nm">Velikka Nirs</div><div class="ls">Last on 5mins ago</div></div></div>
    <div class="mini"><div class="avatar" role="img" aria-label="Suggested person photo"></div><div><div class="nm">Velikka Nirs</div><div class="ls">Last on 5mins ago</div></div></div>
    <div class="mini"><div class="avatar" role="img" aria-label="Suggested person photo"></div><div><div class="nm">Velikka Nirs</div><div class="ls">Last on 5mins ago</div></div></div>
    <div class="mini"><div class="avatar" role="img" aria-label="Suggested person photo"></div><div><div class="nm">Velikka Nirs</div><div class="ls">Last on 5mins ago</div></div></div>
    <div class="mini"><div class="avatar" role="img" aria-label="Suggested person photo"></div><div><div class="nm">Velikka Nirs</div><div class="ls">Last on 5mins ago</div></div></div>
    <div class="mini"><div class="avatar" role="img" aria-label="Suggested person photo"></div><div><div class="nm">Velikka Nirs</div><div class="ls">Last on 5mins ago</div></div></div>
  </div>
  <span class="abs" style="left:26px;top:195px;color:#ccc;font-size:20px">&lsaquo;</span>
  <span class="abs" style="left:220px;top:195px;font-size:20px">&rsaquo;</span>
</section>

<section class="card top-users">
  <div class="card-head upper" style="font-weight:400;height:48px">TOP PRODUCT USERS <svg width="17" height="17"><circle cx="7" cy="7" r="5.5" fill="none" stroke="#ccc" stroke-width="2"/><line x1="11" y1="11" x2="16" y2="16" stroke="#ccc" stroke-width="2"/></svg></div>
  <div class="tu"><div class="avatar" role="img" aria-label="Top user photo"></div><div><div class="nm">Lana Croft</div><div class="ls">Last on: 5mins ago</div></div></div>
  <div class="tu"><div class="avatar" role="img" aria-label="Top user photo"></div><div><div class="nm">Nicka Landmarks</div><div class="ls">Last on: 5mins ago</div></div></div>
  <div class="tu"><div class="avatar" role="img" aria-label="Top user photo"></div><div><div class="nm">Helen Apple</div><div class="ls">Last on: 5mins ago</div></div></div>
  <div class="tu"><div class="avatar" role="img" aria-label="Top user photo"></div><div><div class="nm">Lana Croft</div><div class="ls">Last on: 5mins ago</div></div></div>
  <div class="more"><svg width="8" height="14"><circle cx="4" cy="3" r="2.5" fill="#bbb"/><rect x="2" y="6" width="4" height="8" fill="#bbb"/></svg>More Top Users</div>
</section>

<footer class="footer">Logo - Copyright. All rights reserved.</footer>

</div>
</body>
</html>
```